Logo and packaging design for a food brand: Noble Drippings

Dear designer,

I'm located in Vancouver, British Columbia, Canada, and I'm launching a brand of products made of beef tallow. It's called Noble Drippings. I'm ultimately looking for a designer that can help me build the brand and create a series of products.

Here is what I need at this point:

- A logo for Noble Drippings (playing with the letters N and D - sketch using SketchMind attached)
- A packaging design for the PREMIUM WAGYU TALLOW - 235 ml (= 8 oz: https://www.vessora-supply.example/item/JX-40211/glass-jar-8-oz-black-cap)
- Glass jar with a label all around it and a lid seal label
- Primary colours: black, white, gold
- Secondary colours if needed: Canada red and light grey
- Fonts: not specified, looking forward to your inputs on what works
- Please refer to our #1 competitor as reference: https://www.harlowmeadowfoods.example/collections/items (we like their design style as well)
- #2 competitor to be used as reference: https://brisketbarn.example/items/1-jar-14-0-oz-organic-grass-fed-beef-tallow

- Information for the packaging:
PREMIUM WAGYU BEEF TALLOW
100% PURE
(optional) PRODUCED IN CANADA
NUTRITIONAL VALUE (we don't have the numbers yet, but please create a placeholder/mockup for this section)
* You can also add more information following the example from our Competitor 01

- Please feel free to improve the logo, but keep the concept of Noble Drippings (or ND) + the face of a bull
- Finally, I'd also love to see two colour schemes: one dark and one bright - I hope it's not asking too much

Target Market(s)

North America

Industry/Entity Type

Food

Font styles to use
Sans Serif
Script

Colors
FFC000
F8CF3A
FAE287
FDF2CF
FEFAEE

Requirements
Must have
• Incorporate gold, black and white
Nice to have
• Play with the letters ND in the logo (company name: Noble Drippings)
Should not have
• Many colours

```html
<!DOCTYPE html>
<html lang="en">
<head>
<meta charset="utf-8">
<title>Noble Drippings – Premium Wagyu Beef Tallow Label</title>
<link rel="stylesheet" href="https://fonts.googleapis.com/css2?family=Poppins:wght@500;600&family=Cormorant+Garamond:wght@700&display=swap">
<style>
  :root {
    --page-grey: #cbcbcb;
    --label-black: #121212;
    --panel-dark: #1a1a1a;
    --panel-mid: #262626;
    --white: #ffffff;
    --gold-deep: #b1872a;
    --gold-mid: #d6aa50;
    --gold-light: #fae287;
    --gold-pale: #fdf2b8;
    --ink: #151515;
  }
  * { margin: 0; padding: 0; box-sizing: border-box; }
  html, body { width: 1200px; height: 876px; overflow: hidden; background: var(--page-grey); }
  .canvas { position: relative; width: 1200px; height: 876px; }

  .label {
    position: absolute; left: 106px; top: 105px; width: 991px; height: 653px;
    background: var(--label-black);
    box-shadow: 0 4px 18px rgba(0,0,0,0.18);
    font-family: "Poppins", sans-serif; color: var(--white);
  }

  .brand-header {
    position: absolute; left: 0; top: 0; width: 100%; height: 201px;
    display: flex; justify-content: center; align-items: center; gap: 24px;
  }
  .brand-mark { width: 58px; height: 58px; background: var(--white); }
  .brand-name {
    font-weight: 500; font-size: 46px; line-height: 52px; letter-spacing: 0.5px;
    text-transform: uppercase;
  }

  .grade-band {
    position: absolute; left: 1px; top: 201px; width: 994px; height: 60px;
    background: linear-gradient(90deg, var(--gold-deep) 0%, var(--gold-mid) 18%, var(--gold-light) 45%, var(--gold-pale) 62%, var(--gold-light) 70%, var(--gold-mid) 86%, var(--gold-deep) 100%);
    display: flex; justify-content: center; align-items: center;
    color: var(--ink); font-weight: 600; font-size: 45px; letter-spacing: 11px; padding-left: 11px;
  }

  .product-panel {
    position: absolute; left: 0; top: 261px; width: 100%; height: 392px;
    background: radial-gradient(ellipse at 50% 45%, #0b0b0b 0%, var(--panel-dark) 55%, var(--panel-mid) 100%);
    text-align: center;
  }
  .product-panel[role="img"] { }

  .product-name {
    position: absolute; left: 0; width: 100%;
    font-family: "Cormorant Garamond", serif; font-weight: 700; color: var(--white);
  }
  .product-name--wagyu { top: 20px; font-size: 136px; line-height: 150px; letter-spacing: 2px; }
  .product-name--type { top: 158px; font-size: 62px; line-height: 70px; letter-spacing: 9px; padding-left: 9px; }

  .rule {
    position: absolute; left: 167px; width: 660px; height: 1px;
    background: linear-gradient(90deg, transparent, rgba(255,255,255,0.85) 30%, rgba(255,255,255,0.85) 70%, transparent);
  }
  .rule--top { top: 238px; }
  .rule--bottom { top: 304px; }

  .claims {
    position: absolute; left: 0; top: 256px; width: 100%;
    font-weight: 500; font-size: 20px; line-height: 30px; letter-spacing: 0.3px;
  }
  .claims .dot { margin: 0 10px; }

  .specs {
    position: absolute; left: 0; top: 333px; width: 100%;
    display: flex; justify-content: center; align-items: center;
    font-weight: 500; font-size: 27px; line-height: 34px;
  }
  .specs .divider { width: 1px; height: 35px; background: var(--white); margin: 0 28px 0 34px; }
</style>
</head>
<body>
<div class="canvas">
  <section class="label">
    <header class="brand-header">
      <div class="brand-mark"></div>
      <div class="brand-name">Noble<br>Drippings</div>
    </header>

    <div class="grade-band">PREMIUM</div>

    <div class="product-panel">
      <h1 class="product-name product-name--wagyu">WAGYU</h1>
      <h2 class="product-name product-name--type">BEEF TALLOW</h2>
      <div class="rule rule--top"></div>
      <p class="claims">NO ARTIFICIAL INGRIDIENTS<span class="dot">•</span>GLUTEN FREE<span class="dot">•</span>NO PRESERVATIVES</p>
      <div class="rule rule--bottom"></div>
      <div class="specs">
        <span>NET WT. 8 OZ</span>
        <span class="divider"></span>
        <span>100% PURE</span>
      </div>
    </div>
  </section>
</div>
</body>
</html>
```